Willow Ember Uniform Label Redesign

To refine our current product label designs into one, simple, modern, crisp, general look that can be adapted to all our all Natural Skin Care and Wellness products. I am inspired by the elegant versatility of products like Corvalis Botanic Beauty or Tidal Beauty label schemes. We no longer want labels that indicate scent or ingredients. We have two primary colors that we want to maintain (#096CA3 and #DEE33F), and are willing to entertain subtle additions of others, other than black. Our labels will be printed on white or clear material. We use mainly Cosmo or Boston Round container shapes, plus flat top, smooth, round jars. Maybe a faded watermark highlight the "natural" or "beautiful" side of our products. we need to convey confidence, while remaining simple. We currently use the Advantage font. Maybe Century Gothic may work. Something similar that is easy on the eyes. Maybe vertical main text? We are willing to entertain a lot of ideas. These designs will offer ideas into our eventual Website (www.willowember.com) redesign.

Target Market(s)

Those who are familiar with the power of natural, plant based skin care and wellness products

Industry/Entity Type

Natural Skin Care and Wellness

Font styles to use
Sans Serif
Other font styles liked:
• Century Gothic, Advantage, or similar that is easy on the eyes

Colors
0054AA
0677BA
7BADD7
CADEEF
E8F1F8
59FF00
82FF00
B8FF75
E3FFCB
F4FFEA

Requirements
Must have
• "Clean Lines"; These colors: (#096CA3 and #DEE33F)
Nice to have
• MAYBE vertical main text or a watermark image

```html
<!DOCTYPE html>
<html lang="en">
<head>
<meta charset="utf-8">
<title>Willow Ember – Green Tea Hydrating Serum Label</title>
<link rel="stylesheet" href="https://fonts.googleapis.com/css2?family=Questrial&display=swap">
<style>
  :root {
    --brand-blue: #096CA3;
    --brand-lime: #DEE33F;
    --label-cream: #F7F8DC;
    --label-cream-deep: #EEF1C4;
    --ink-dark: #2B2B1E;
    --stage-olive: #48490C;
    --leaf-green: #7DB343;
    --leaf-light: #C9E3A4;
  }
  * { margin: 0; padding: 0; box-sizing: border-box; }
  html, body {
    width: 1056px;
    height: 1200px;
    overflow: hidden;
    background: var(--stage-olive);
    font-family: "Questrial", "Century Gothic", sans-serif;
  }
  .canvas {
    position: relative;
    width: 1056px;
    height: 1200px;
    display: flex;
    align-items: center;
    justify-content: center;
  }
  .label {
    position: relative;
    width: 720px;
    height: 960px;
    background: linear-gradient(180deg, var(--label-cream) 0%, var(--label-cream-deep) 100%);
    border-top: 16px solid var(--brand-lime);
    border-bottom: 16px solid var(--brand-lime);
    display: flex;
    flex-direction: column;
    align-items: center;
    text-align: center;
    color: var(--brand-blue);
  }
  .brand-name {
    margin-top: 110px;
    font-size: 78px;
    font-weight: 400;
    letter-spacing: 1px;
    line-height: 1;
  }
  .tagline {
    margin-top: 22px;
    font-size: 30px;
    color: var(--ink-dark);
    letter-spacing: 0.5px;
  }
  .hero-art {
    margin-top: 90px;
    width: 520px;
    height: 300px;
    border-radius: 50%;
    background: radial-gradient(ellipse at 45% 55%, var(--leaf-green) 0%, var(--leaf-light) 45%, rgba(247,248,220,0) 72%);
  }
  .product-name {
    margin-top: 70px;
    font-size: 56px;
    line-height: 1.12;
    font-weight: 400;
  }
  .product-note {
    margin-top: 16px;
    font-size: 30px;
    color: var(--ink-dark);
  }
  .net-weight {
    position: absolute;
    bottom: -16px;
    left: 50%;
    transform: translateX(-50%);
    padding: 14px 40px 18px;
    background: var(--brand-lime);
    border-radius: 16px 16px 0 0;
    font-size: 28px;
    color: var(--ink-dark);
  }
</style>
</head>
<body>
  <main class="canvas">
    <section class="label">
      <h1 class="brand-name">Willow Ember</h1>
      <p class="tagline">Simple. Beautiful. Timeless</p>
      <div class="hero-art" role="img" aria-label="Illustration of green tea leaves swirling in a clear water splash"></div>
      <h2 class="product-name">Green Tea<br>Hydrating Serum</h2>
      <p class="product-note">with Hyaluronic Acid</p>
      <p class="net-weight">Net Weight 40oz</p>
    </section>
  </main>
</body>
</html>
```